Business Card

The design you sent was fine. I just need the logo changed on one side. The back needs to have the text "Vell Marrow Group" next to the log and the words "Insight Balance Resolve" in the middle. The front logo needs to have the "Vell Marrow Advisory" logo attached

Colors

Designer to choose colors to be used in the design.

```html
<!DOCTYPE html>
<html lang="en">
<head>
<meta charset="utf-8">
<title>Vell Marrow Advisory – Business Card</title>
<link rel="stylesheet" href="https://fonts.googleapis.com/css2?family=Open+Sans:wght@400;600;700&display=swap">
<style>
  :root {
    --backdrop: #2e2e2e;
    --brand-blue: #00bde3;
    --card-white: #ffffff;
    --ink: #1a1a1a;
    --ink-soft: #333333;
    --rule: #1a1a1a;
  }
  * { box-sizing: border-box; margin: 0; padding: 0; }
  html, body {
    width: 1200px; height: 866px; overflow: hidden;
    background: var(--backdrop);
    font-family: "Open Sans", Arial, sans-serif;
  }
  .canvas {
    width: 1200px; height: 866px;
    display: flex; flex-direction: column;
    align-items: center; justify-content: center; gap: 52px;
  }
  .card {
    position: relative;
    width: 630px; height: 360px;
    overflow: hidden;
    box-shadow: 0 10px 24px rgba(0,0,0,.45);
  }

  /* Front */
  .card--front { background: var(--card-white); }
  .card--front::after {
    content: ""; position: absolute; left: 0; right: 0; bottom: 0;
    height: 10px; background: var(--brand-blue);
  }
  .brand-lockup {
    position: absolute; left: 44px; top: 44px;
    display: flex; align-items: center; gap: 16px;
  }
  .brand-mark {
    width: 46px; height: 46px; border-radius: 50%;
    background: var(--brand-blue); flex: none;
  }
  .brand-name {
    font-weight: 700; font-size: 34px; line-height: 1;
    color: var(--ink); letter-spacing: .2px;
  }
  .brand-tagline {
    position: absolute; left: 106px; top: 104px;
    font-size: 10.5px; font-weight: 600; color: var(--ink-soft);
    padding-top: 7px; border-top: 1.5px solid var(--rule);
    letter-spacing: .2px;
  }
  .person {
    position: absolute; left: 44px; top: 156px;
  }
  .person-name {
    font-size: 19px; font-weight: 700; color: var(--brand-blue);
    letter-spacing: 1px; text-transform: uppercase; line-height: 1.1;
  }
  .person-role {
    font-size: 15px; color: var(--ink-soft); margin-top: 2px;
  }
  .contact-list {
    list-style: none; margin-top: 12px;
    font-family: Arial, "Open Sans", sans-serif;
  }
  .contact-list li {
    display: flex; align-items: center; gap: 9px;
    font-size: 15px; color: var(--ink-soft); line-height: 1.45;
  }
  .contact-list svg { width: 15px; height: 15px; flex: none; }
  .contact-web .accent { color: var(--brand-blue); }
  .address {
    position: absolute; right: 44px; bottom: 34px;
    font-family: Arial, "Open Sans", sans-serif;
    font-style: normal;
    font-size: 15px; color: var(--ink-soft); line-height: 1.35;
    text-align: left; letter-spacing: .5px;
  }

  /* Back */
  .card--back {
    background: var(--brand-blue);
    display: flex; flex-direction: column;
    align-items: center; justify-content: center;
    color: var(--card-white);
  }
  .back-lockup { display: flex; align-items: center; gap: 18px; }
  .back-mark {
    width: 58px; height: 58px;
    border: 4px solid var(--card-white); flex: none;
  }
  .back-name {
    font-size: 40px; font-weight: 600; line-height: 1;
  }
  .back-motto {
    margin-top: 16px; font-size: 19px; font-weight: 400;
    letter-spacing: .3px;
  }
</style>
</head>
<body>
<main class="canvas">

  <section class="card card--front" aria-label="Card front">
    <div class="brand-lockup">
      <span class="brand-mark"></span>
      <span class="brand-name">Vell Marrow Advisory</span>
    </div>
    <p class="brand-tagline">Steady Counsel delivering Lasting Clarity Daily</p>

    <div class="person">
      <p class="person-name">Dorian Pell</p>
      <p class="person-role">Managing Director</p>
      <ul class="contact-list">
        <li>
          <svg viewBox="0 0 16 16" aria-hidden="true"><rect x="1" y="1" width="14" height="14" rx="3" fill="none" stroke="var(--brand-blue)" stroke-width="1.6"/><path d="M5.5 4.2l1.4 1.6-.9 1c.5 1.2 1.4 2.1 2.6 2.6l1-.9 1.6 1.4-.9 1.3C7.8 11 5 8.2 4.2 5.1z" fill="var(--brand-blue)"/></svg>
          031-555 204 118
        </li>
        <li>
          <svg viewBox="0 0 16 16" aria-hidden="true"><rect x="1" y="3" width="14" height="10" fill="var(--brand-blue)"/><path d="M1 3l7 6 7-6" fill="none" stroke="#fff" stroke-width="1.3"/></svg>
          hello@vellmarrow.com
        </li>
        <li class="contact-web">
          <svg viewBox="0 0 16 16" aria-hidden="true"><circle cx="8" cy="8" r="7" fill="var(--brand-blue)"/><path d="M1 8h14M8 1c-3 3.5-3 10.5 0 14M8 1c3 3.5 3 10.5 0 14M2.5 4.5h11M2.5 11.5h11" fill="none" stroke="#fff" stroke-width=".9"/></svg>
          <span>www.<span class="accent">vellmarrow</span>.com</span>
        </li>
      </ul>
    </div>

    <address class="address">
      88, Quarry Lane<br>
      Harlow Vale, 30718
    </address>
  </section>

  <section class="card card--back" aria-label="Card back">
    <div class="back-lockup">
      <span class="back-mark"></span>
      <span class="back-name">Vell Marrow Group</span>
    </div>
    <p class="back-motto">Insight Balance Resolve</p>
  </section>

</main>
</body>
</html>
```